buseisness card

design a card that similar to my web site
BRIXENTAPLORLLC .COM

Contact Information for Business Card

NAME PHONE # WEBSITE EMAIL AND DISCTIPTION OF WHAT WE DO

Colors
0054AA
0677BA
7BADD7
CADEEF
E8F1F8

Requirements
Must have
• lOGO AND DETAILS
Nice to have
• I LIKE THE WATER LIKE ON MY WEB SITE

```html
<!DOCTYPE html>
<html lang="en">
<head>
<meta charset="utf-8">
<title>Brixentaplor Business Card</title>
<link rel="stylesheet" href="https://fonts.googleapis.com/css2?family=Montserrat:wght@600;700&family=Roboto:ital,wght@0,400;0,700;1,400&display=swap">
<style>
  :root {
    --blue-deep: #0054AA;
    --blue-mid: #0677BA;
    --blue-soft: #7BADD7;
    --blue-pale: #CADEEF;
    --blue-mist: #E8F1F8;
    --cyan-glow: #6fd3ea;
    --white: #ffffff;
    --backdrop: #e9edf2;
  }
  * { box-sizing: border-box; margin: 0; padding: 0; }
  html, body { width: 1200px; height: 900px; overflow: hidden; }
  body {
    background: var(--backdrop);
    font-family: "Roboto", Arial, sans-serif;
    position: relative;
  }
  .card {
    position: absolute;
    left: 290px;
    width: 620px;
    height: 354px;
    border-radius: 22px;
    overflow: hidden;
    box-shadow: 0 10px 30px rgba(0, 40, 90, 0.18);
  }
  .card-front { top: 66px; background: var(--white); }
  .card-back {
    top: 480px;
    background: linear-gradient(135deg, #1a6fc6 0%, var(--blue-deep) 100%);
    display: flex;
    align-items: center;
    justify-content: center;
  }
  .wave { position: absolute; inset: 0; width: 100%; height: 100%; }
  .brand {
    position: absolute;
    display: flex;
    align-items: center;
    gap: 12px;
    font-family: "Montserrat", Arial, sans-serif;
    font-weight: 600;
    letter-spacing: 3px;
  }
  .brand-front { left: 250px; top: 112px; font-size: 25px; color: var(--blue-mid); }
  .brand-back { position: static; font-size: 32px; color: var(--white); }
  .brand-dot {
    width: 40px; height: 40px; border-radius: 50%;
    background: var(--blue-mid);
  }
  .brand-back .brand-dot { background: var(--blue-soft); width: 48px; height: 48px; }
  .person {
    position: absolute; left: 40px; top: 232px;
    color: var(--white); text-align: right; width: 230px;
  }
  .person-name { font-weight: 700; font-size: 22px; letter-spacing: 0.5px; }
  .person-title { font-style: italic; font-size: 14px; margin-top: 3px; }
  .divider {
    position: absolute; left: 288px; top: 232px;
    width: 1px; height: 54px; background: rgba(255,255,255,0.7);
  }
  .contacts {
    position: absolute; left: 304px; top: 230px;
    list-style: none; color: var(--white); font-size: 14px; line-height: 19px;
  }
  .contacts li { display: flex; align-items: center; gap: 8px; }
  .contacts svg { width: 12px; height: 12px; fill: none; stroke: var(--white); stroke-width: 1.6; }
  .address {
    position: absolute; left: 40px; top: 310px;
    color: var(--white); font-size: 14px; letter-spacing: 0.3px;
  }
</style>
</head>
<body>
  <section class="card card-front">
    <svg class="wave" viewBox="0 0 620 354" preserveAspectRatio="none" aria-hidden="true">
      <defs>
        <linearGradient id="sea" x1="0" y1="0" x2="0" y2="1">
          <stop offset="0" stop-color="#3fb6e0"/>
          <stop offset="0.45" stop-color="var(--blue-mid)"/>
          <stop offset="1" stop-color="var(--blue-deep)"/>
        </linearGradient>
      </defs>
      <path d="M0,120 C150,150 300,230 620,262 L620,354 L0,354 Z" fill="url(#sea)"/>
      <path d="M0,116 C150,146 300,226 620,258" fill="none" stroke="var(--cyan-glow)" stroke-width="6" opacity="0.8"/>
      <path d="M0,132 C170,170 320,236 620,282" fill="none" stroke="var(--blue-pale)" stroke-width="2" opacity="0.7"/>
      <path d="M0,150 C190,192 340,252 620,300" fill="none" stroke="var(--cyan-glow)" stroke-width="3" opacity="0.5"/>
    </svg>
    <div class="brand brand-front"><span class="brand-dot"></span>BRIXENTAPLOR</div>
    <div class="person">
      <p class="person-name">DAREN HOLT</p>
      <p class="person-title">Founder &amp; CEO</p>
    </div>
    <span class="divider"></span>
    <ul class="contacts">
      <li><svg viewBox="0 0 12 12"><path d="M2,1 L4.5,1 L5,4 L3.5,5 C4.3,6.8 5.2,7.7 7,8.5 L8,7 L11,7.5 L11,10 C6,11 1,6 2,1 Z"/></svg>+740 555 0147</li>
      <li><svg viewBox="0 0 12 12"><rect x="1" y="2.5" width="10" height="7"/><path d="M1,2.5 L6,6.5 L11,2.5"/></svg>dh@bx204.com</li>
      <li><svg viewBox="0 0 12 12"><circle cx="6" cy="6" r="5"/><path d="M1,6 L11,6 M6,1 C3.5,4 3.5,8 6,11 M6,1 C8.5,4 8.5,8 6,11"/></svg>www.brixentaplorllc.com</li>
    </ul>
    <p class="address">1840 Harbor Crest Drive Lakeview, OH 43950</p>
  </section>

  <section class="card card-back">
    <div class="brand brand-back">BRIXENTAPLOR<span class="brand-dot"></span></div>
  </section>
</body>
</html>
```